Software Company Requires Website

We need a web design for a new mobile software development company based in London named Velmark Solutions.
The design needs to be clean and smooth. Not too flashy, not too boring.
I would like to try the design with some warm colors, and maybe a headline or something highlighted with a strong color. ( logo ? ) The layout should be something like the bellow links, all in one page.

http://quorbit.example/
http://www.telvane.example/
http://www.work-plover.example/
http://www.brisk.example/
http://www.fenlowtech.example/us/

Now some of them they seem different from the others, but in each of them there is something that ticks my brain, so it`s up to you to surprise me.

I have uploaded the logo of the company, so you guys can fit that in your design as well.
Updates

Hy everybody This will be the last update for the brief. The company will focus in the beginning for mobile development only, so i would like the website design to be done in a matter that will reflect that. We will develop IORIA, Andara and Windows applications. We will also require 3 pages: One for the home menu, one for portfolio and one for contact us. The layout should be the same ( one page scroll down ) but the design of the 3 pages different. Please readdress the brief. Hope that i provided enough information for the scope of the project.

I have uploaded the logo that you guys can use. If the logo requires small modifications you can adjust that to suit your idea as long as the logo does not change completely.

Target Market(s)

High End companies that require simplified software solutions.

Industry/Entity Type

It Company

Number of Pages Required

3 page

Requirements
Must have
• One page scroll down layout for 3 pages:
• one for home page, one for portfolio and one for contact us.
• In the portfolio page we would like to have different display options for given examples of applications ( min 3 )

```html
<!DOCTYPE html>
<html lang="en">
<head>
<meta charset="utf-8">
<title>Velmark Solutions — Mobile App Development</title>
<link href="https://fonts.googleapis.com/css2?family=Open+Sans:wght@400;600;700&display=swap" rel="stylesheet">
<style>
:root{
  --blue:#2a7bc4;
  --blue-dark:#1f63a3;
  --ink:#3f3f3f;
  --muted:#a9a9a9;
  --light:#ebebeb;
  --dark:#1d1d1d;
  --darker:#111111;
  --white:#ffffff;
  --grey-circle:#dcdcdc;
}
*{box-sizing:border-box;margin:0;padding:0}
html,body{width:1200px;height:4196px;overflow:hidden}
body{position:relative;font-family:"Open Sans",Arial,sans-serif;color:var(--ink);background:var(--white)}
.abs{position:absolute}
.section-title{position:absolute;left:0;width:1200px;text-align:center;font-size:34px;font-weight:600;color:var(--ink)}
.section-sub{position:absolute;left:235px;width:730px;text-align:center;font-size:13px;line-height:25px;color:var(--muted)}

/* header */
.site-header{position:absolute;left:0;top:0;width:1200px;height:84px;background:var(--dark)}
.brand{position:absolute;left:106px;top:22px;display:flex;align-items:center;gap:12px;color:var(--white);font-size:26px;font-weight:600}
.brand-mark{width:36px;height:36px;border:3px solid var(--white)}
.main-nav{position:absolute;left:587px;top:0;height:84px;display:flex}
.main-nav a{display:block;height:84px;line-height:84px;padding:0 18px;font-size:14px;color:var(--white);text-decoration:none;text-transform:uppercase;font-weight:600}
.main-nav a.active{background:#000;padding:0 20px;color:#9cc8f0}

/* hero */
.hero{position:absolute;left:0;top:84px;width:1200px;height:705px;background:linear-gradient(160deg,#3a8fd6 0%,#2a7bc4 55%,#2369ad 100%)}
.hero-copy{position:absolute;left:117px;width:443px;text-align:right;color:var(--white)}
.hero-kicker{top:115px;font-size:17px;font-weight:700;letter-spacing:.5px}
.hero-title{top:140px;font-size:40px;font-weight:700;line-height:48px}
.hero-text{font-size:13px;line-height:21px;color:#d6e7f7}
.hero-btn{position:absolute;left:344px;top:467px;width:216px;height:44px;border-radius:3px;background:linear-gradient(#f8f8f8,#d8d8d8);color:#333;font-size:14px;font-weight:600;text-align:center;line-height:44px}
.platforms{position:absolute;left:392px;top:540px;display:flex;gap:38px}
.platforms span{width:34px;height:34px;border-radius:50%;background:rgba(255,255,255,.35)}
.hero-devices{position:absolute;left:649px;top:70px;width:442px;height:573px;border-radius:24px;background:linear-gradient(150deg,#2b2b2b,#0c0c0c 60%,#3a2a3a)}

.hex{position:absolute;left:558px;width:84px;height:90px}

/* apps */
.app-phone{position:absolute;left:229px;top:973px;width:261px;height:495px;border-radius:36px;background:linear-gradient(#1a1a1a,#4a2a2a 50%,#1a1a1a)}
.app-heading{position:absolute;left:537px;top:1054px;font-size:15px;font-weight:700;line-height:28px;color:var(--ink)}
.app-text{position:absolute;left:537px;width:442px;font-size:12.5px;line-height:17.5px;color:#8a8a8a}
.store-badge{position:absolute;top:1323px;width:162px;height:53px;border-radius:6px;background:#2b2b2b;border:2px solid #9a9a9a}
.slider-arrow{position:absolute;top:1189px;width:56px;height:56px;border-radius:50%;background:#cfcfcf}

/* services */
.services{position:absolute;left:0;top:1524px;width:1200px;height:560px;background:var(--light)}
.service{position:absolute;top:206px;width:240px;text-align:center}
.service-icon{width:134px;height:134px;margin:0 auto;border-radius:50%;background:var(--grey-circle);border:6px solid #f3f3f3;box-shadow:0 0 0 2px #d0d0d0;display:flex;align-items:center;justify-content:center}
.service-icon.active{background:var(--blue);box-shadow:0 0 0 2px var(--blue)}
.service h3{margin-top:23px;font-size:14px;font-weight:700;color:var(--ink)}
.service p{margin:8px auto 0;width:220px;font-size:12.5px;line-height:18px;color:#9a9a9a}

/* portfolio */
.tile{position:absolute;width:322px;height:202px}
.tile-overlay{background:#3d3d3d;color:var(--white);text-align:center;padding-top:58px}
.tile-overlay h4{font-size:16px;font-weight:700}
.tile-overlay p{margin:8px auto 0;width:250px;font-size:12px;line-height:17px;color:#ddd}
.tile-overlay .dots{margin-top:12px;display:flex;justify-content:center;gap:14px}
.tile-overlay .dots span{width:22px;height:22px;border-radius:50%;background:#777}

/* contact */
.contact{position:absolute;left:0;top:2965px;width:1200px;height:517px;background:var(--blue)}
.contact .section-title{color:var(--white)}
.contact .section-sub{color:#79b2e6}
.field{position:absolute;background:rgba(255,255,255,.28);color:rgba(255,255,255,.75);font-size:13px;padding:14px 14px;text-transform:uppercase}
.send-btn{position:absolute;left:129px;top:417px;width:939px;height:53px;background:rgba(255,255,255,.3);color:rgba(255,255,255,.8);font-size:13px;text-align:center;line-height:53px;text-transform:uppercase}

.map{position:absolute;left:0;top:3482px;width:1200px;height:400px;background:linear-gradient(135deg,#e9e9e9,#dedede 60%,#e6e6e6)}

/* footer */
.site-footer{position:absolute;left:0;top:3882px;width:1200px;height:266px;background:var(--dark);color:#9a9a9a}
.footer-col{position:absolute;top:36px}
.footer-col h5{font-size:15px;font-weight:600;color:var(--white);margin-bottom:12px}
.footer-links a{display:block;font-size:12px;line-height:23px;color:#9a9a9a;text-decoration:none}
.post{display:flex;gap:11px;margin-bottom:26px}
.post-thumb{width:84px;height:62px;background:linear-gradient(135deg,#e07a2a,#3a3a4a)}
.post-thumb.alt{background:linear-gradient(135deg,#2d3f5a,#1a1a1a)}
.post p{width:200px;font-size:11.5px;line-height:16px}
.post strong{color:var(--white);font-weight:600}
.newsletter p{width:230px;font-size:11.5px;line-height:16px}
.newsletter .input{margin-top:14px;width:227px;height:31px;background:var(--white);color:#999;font-size:11px;line-height:31px;padding-left:8px}
.newsletter .btn{margin-top:13px;width:98px;height:32px;background:#3a3a3a;border:1px solid #555;color:var(--white);font-size:13px;text-align:center;line-height:30px}
.social{display:grid;grid-template-columns:repeat(5,28px);gap:19px 17px}
.social span{width:28px;height:28px;background:#3a3a3a}
.social span.primary{background:#2f5fa8}
.to-top{position:absolute;left:1038px;top:188px;width:53px;height:47px;background:#2a2a2a}
.copyright{position:absolute;left:0;top:4148px;width:1200px;height:48px;background:var(--darker);color:#777;font-size:11.5px;text-align:center;line-height:48px}
</style>
</head>
<body>

<header class="site-header">
  <div class="brand"><span class="brand-mark"></span>Velmark Solutions</div>
  <nav class="main-nav">
    <a class="active" href="#">Home</a>
    <a href="#">About Us</a>
    <a href="#">Our Services</a>
    <a href="#">Portfolio</a>
    <a href="#">Contact Us</a>
  </nav>
</header>

<section class="hero" role="img" aria-label="Blue backdrop with a faint city skyline">
  <div class="hero-copy hero-kicker">SPECIALIZED IN ANDARA IORIA</div>
  <h1 class="hero-copy hero-title">Be Creative With<br>Our Development Apps!</h1>
  <p class="hero-copy hero-text" style="top:258px">Lorem ipsum dolor sit amet, consectetur adipiscing elit, sed do eiusmod tempor incididunt ut labore et dolore magna aliqua. Ut enim ad minim veniam, quis nostrud exercitation ullamco laboris nisi ut aliquip ex ea commodo consequat.</p>
  <p class="hero-copy hero-text" style="top:356px">Duis aute irure dolor in reprehenderit in voluptate velit esse cillum dolore eu fugiat nulla pariatur. Excepteur sint occaecat cupidatat non proident, sunt in culpa qui officia deserunt mollit anim id est laborum.</p>
  <div class="hero-btn">Click Here To Learn More</div>
  <div class="platforms"><span></span><span></span><span></span></div>
  <div class="hero-devices" role="img" aria-label="Phone and tablet showing the Velmark Solutions app"></div>
</section>

<svg class="hex" style="top:746px" viewBox="0 0 84 90" aria-hidden="true">
  <polygon points="42,2 80,24 80,66 42,88 4,66 4,24" fill="#ffffff"/>
  <polygon points="42,10 73,28 73,62 42,80 11,62 11,28" fill="#2a7bc4"/>
  <polygon points="42,26 58,35 58,55 42,64 26,55 26,35" fill="none" stroke="#fff" stroke-width="3"/>
  <polyline points="35,42 42,50 49,42" fill="none" stroke="#fff" stroke-width="3"/>
</svg>

<h2 class="section-title" style="top:850px">Yes, We Develop Mobile Apps</h2>
<p class="section-sub" style="top:904px">Lorem ipsum dolor sit amet, consectetur adipiscing elit, sed do eiusmod tempor incididunt ut labore et dolore magna aliqua.</p>

<div class="slider-arrow" style="left:112px"><svg width="56" height="56" viewBox="0 0 56 56"><polyline points="32,18 22,28 32,38" fill="none" stroke="#fff" stroke-width="4"/></svg></div>
<div class="app-phone" role="img" aria-label="Phone playing a music video"></div>
<h3 class="app-heading">LOREM IPSUM DOLOR SIT<br>AMET CONSECTETUR ADIPISCING ELIT</h3>
<p class="app-text" style="top:1124px">Lorem ipsum dolor sit amet, consectetur adipiscing elit, sed do eiusmod tempor incididunt ut labore et dolore magna aliqua. Ut enim ad minim veniam, quis nostrud exercitation ullamco laboris nisi ut aliquip ex ea commodo consequat.</p>
<p class="app-text" style="top:1213px">Duis aute irure dolor in reprehenderit in voluptate velit esse cillum dolore eu fugiat nulla pariatur. Excepteur sint occaecat cupidatat non proident, sunt in culpa qui officia deserunt mollit anim id est laborum.</p>
<div class="store-badge" style="left:537px"></div>
<div class="store-badge" style="left:713px"></div>
<div class="slider-arrow" style="left:1032px"><svg width="56" height="56" viewBox="0 0 56 56"><polyline points="24,18 34,28 24,38" fill="none" stroke="#fff" stroke-width="4"/></svg></div>

<section class="services">
  <h2 class="section-title" style="top:42px">Check Our Featured Services</h2>
  <p class="section-sub" style="top:95px">Lorem ipsum dolor sit amet, consectetur adipiscing elit, sed do eiusmod tempor incididunt ut labore et dolore magna aliqua.</p>

  <div class="service" style="left:109px">
    <div class="service-icon active"><svg width="60" height="60" viewBox="0 0 60 60" fill="none" stroke="#fff" stroke-width="3"><rect x="18" y="6" width="24" height="48" rx="4"/><line x1="26" y1="48" x2="34" y2="48"/></svg></div>
    <h3>LOREM IPSUM DOLOR SIT</h3>
    <p>Lorem ipsum dolor sit amet, consectetur adipiscing elit, sed do eiusmod tempor incididunt ut labore et dolore magna aliqua.</p>
  </div>
  <div class="service" style="left:355px">
    <div class="service-icon"><svg width="60" height="60" viewBox="0 0 60 60" fill="none" stroke="#fff" stroke-width="3"><path d="M8 26c0-9 10-16 22-16s22 7 22 16-10 16-22 16c-3 0-6 0-8-1l-10 7 3-10c-4-3-7-7-7-12z"/></svg></div>
    <h3>LOREM IPSUM DOLOR SIT</h3>
    <p>Lorem ipsum dolor sit amet, consectetur adipiscing elit, sed do eiusmod tempor incididunt ut labore et dolore magna aliqua.</p>
  </div>
  <div class="service" style="left:602px">
    <div class="service-icon"><svg width="60" height="60" viewBox="0 0 60 60" fill="none" stroke="#fff" stroke-width="3"><path d="M16 42H8V10h44v32h-8"/><polygon points="30,30 44,50 16,50"/></svg></div>
    <h3>LOREM IPSUM DOLOR SIT</h3>
    <p>Lorem ipsum dolor sit amet, consectetur adipiscing elit, sed do eiusmod tempor incididunt ut labore et dolore magna aliqua.</p>
  </div>
  <div class="service" style="left:851px">
    <div class="service-icon"><svg width="60" height="60" viewBox="0 0 60 60" fill="none" stroke="#fff" stroke-width="3"><circle cx="30" cy="30" r="8"/><path d="M30 8v8M30 44v8M8 30h8M44 30h8M14 14l6 6M40 40l6 6M14 46l6-6M40 20l6-6"/><circle cx="30" cy="30" r="16"/></svg></div>
    <h3>LOREM IPSUM DOLOR SIT</h3>
    <p>Lorem ipsum dolor sit amet, consectetur adipiscing elit, sed do eiusmod tempor incididunt ut labore et dolore magna aliqua.</p>
  </div>
</section>

<h2 class="section-title" style="top:2117px">Our Portfolio</h2>
<p class="section-sub" style="top:2171px">Lorem ipsum dolor sit amet, consectetur adipiscing elit, sed do eiusmod tempor incididunt ut labore et dolore magna aliqua.</p>

<div class="tile" style="left:109px;top:2254px;height:412px;background:linear-gradient(150deg,#5b8fd0,#1d1d2a 55%,#a04a6a)" role="img" aria-label="Close-up of app icons on a phone screen"></div>
<div class="tile" style="left:439px;top:2254px;background:linear-gradient(135deg,#8a2a55,#d07a9a 60%,#f0d0dc)" role="img" aria-label="Beauty brand app on tablet and phones"></div>
<div class="tile" style="left:769px;top:2254px;background:linear-gradient(135deg,#2e8a3a,#b43a2a 60%,#3a2a1a)" role="img" aria-label="Restaurant ordering app on phones"></div>
<div class="tile tile-overlay" style="left:439px;top:2464px">
  <h4>LOREM IPSUM DOLOR</h4>
  <p>Lorem ipsum dolor sit amet consectetur adipiscing elit, Sed do eiusmod tempor incidunt magna aliqua.</p>
  <div class="dots"><span></span><span></span></div>
</div>
<div class="tile" style="left:769px;top:2464px;height:412px;background:linear-gradient(#1a1a1a,#111 50%,#2a2a2a)" role="img" aria-label="Fitness tracker app summary screen"></div>
<div class="tile" style="left:109px;top:2674px;background:linear-gradient(135deg,#f2f2f2,#d9d9d9 60%,#e8b0a0)" role="img" aria-label="Mobile application development artwork"></div>
<div class="tile" style="left:439px;top:2674px;background:linear-gradient(135deg,#0e2a4a,#1e7ad0 55%,#0a1a30)" role="img" aria-label="Hand touching glowing app icons"></div>

<section class="contact">
  <h2 class="section-title" style="top:43px">Keep In Touch</h2>
  <p class="section-sub" style="top:94px">Lorem ipsum dolor sit amet, consectetur adipiscing elit, sed do eiusmod tempor incididunt ut labore et dolore magna aliqua.</p>
  <div class="field" style="left:129px;top:179px;width:456px;height:53px">Name</div>
  <div class="field" style="left:129px;top:252px;width:456px;height:53px">E-mail</div>
  <div class="field" style="left:129px;top:324px;width:456px;height:53px">Subject</div>
  <div class="field" style="left:615px;top:179px;width:453px;height:198px">Your Message</div>
  <div class="send-btn">Send Email</div>
</section>

<svg class="hex" style="top:2918px" viewBox="0 0 84 90" aria-hidden="true">
  <polygon points="42,2 80,24 80,66 42,88 4,66 4,24" fill="#ffffff"/>
  <polygon points="42,10 73,28 73,62 42,80 11,62 11,28" fill="#2a7bc4"/>
  <polygon points="42,26 58,35 58,55 42,64 26,55 26,35" fill="none" stroke="#fff" stroke-width="3"/>
  <polyline points="35,42 42,50 49,42" fill="none" stroke="#fff" stroke-width="3"/>
</svg>

<div class="map" role="img" aria-label="Street map of the office area in London">
  <svg class="abs" style="left:78px;top:94px" width="46" height="62" viewBox="0 0 46 62"><path d="M23 2C11 2 2 11 2 23c0 15 21 37 21 37s21-22 21-37C44 11 35 2 23 2z" fill="#111"/><circle cx="23" cy="22" r="8" fill="#e6e6e6"/></svg>
  <svg class="abs" style="left:920px;top:253px" width="46" height="62" viewBox="0 0 46 62"><path d="M23 2C11 2 2 11 2 23c0 15 21 37 21 37s21-22 21-37C44 11 35 2 23 2z" fill="#111"/><circle cx="23" cy="22" r="8" fill="#e6e6e6"/></svg>
</div>

<footer class="site-footer">
  <div class="footer-col footer-links" style="left:109px">
    <h5>Site Links</h5>
    <a href="#">Home</a><a href="#">About Us</a><a href="#">Our Services</a><a href="#">Portfolio</a><a href="#">Contact Us</a>
  </div>
  <div class="footer-col" style="left:260px">
    <h5>Recent Blog Posts</h5>
    <div class="post"><div class="post-thumb"></div><p><strong>Lorem Ipsum Dolor Sit Amet,</strong><br>consectetur adipiscing elit, sed do eiusmod tempor incidunt magna aliqua.</p></div>
    <div class="post"><div class="post-thumb alt"></div><p><strong>Lorem Ipsum Dolor Sit Amet,</strong><br>consectetur adipiscing elit, sed do eiusmod tempor incidunt magna aliqua.</p></div>
  </div>
  <div class="footer-col newsletter" style="left:587px">
    <h5>Subscribe Our Newsletter</h5>
    <p>Enter your email address &amp; get subscribe our newsletter.</p>
    <div class="input">Enter your email address...</div>
    <div class="btn">Subscribe</div>
  </div>
  <div class="footer-col" style="left:887px">
    <h5>Follow Us</h5>
    <div class="social"><span class="primary"></span><span></span><span></span><span></span><span></span><span></span><span></span><span></span></div>
  </div>
  <div class="to-top"><svg width="53" height="47" viewBox="0 0 53 47"><polyline points="20,27 26.5,20 33,27" fill="none" stroke="#ccc" stroke-width="3"/></svg></div>
</footer>

<div class="copyright">Copyrights ©2014 VelmarkSolutions.example - All Rights reserved</div>

</body>
</html>
```